Hopscotch Nell needs updated Marketing Material!

Moving business to a new location and am looking to update all marketing material, including business cards, postcards, flyers, website. I've attached a copy of my current business card.
Updates

Good Morning!  I just received my new business phone number.  It is 583-402-9176

Hello All Designers!

Thank you for all the submissions I have received so far!  I wanted to give you a bit more background on what Hopscotch Nell is all about:

I started this service when I was downsized out of a sales and marketing position.   A friend asked if I had time to run a few errands for her while she was at work.  "Lightbulb"!  I thought there must be more people that are over worked, over booked and want nothing more to do when they get home than spend time with their families or just relaxing.  And who wants to do all their running around on the weekends??  Hopscotch Nell was born!

I have been extremely fortunate with my business here in California.  However, this summer I will be moving to a small town in Pennsylvania and I will be in uncharted territory.  I hope to have marketing material that will "WOW" all new potential clients.  Letting them know that I offer a unique service that can put time back into their week and free up their weekends for more important things.

If there is anything else I can tell you in order to help you with your design process, please let me know!
Thank you!
Nellie

Target Market(s)

Busy working parents and young professionals with disposable income that would like to spend their down time doing things that they enjoy rather than doing errands.

Industry/Entity Type

Marketing

```html
<!DOCTYPE html>
<html lang="en">
<head>
<meta charset="utf-8">
<title>Hopscotch Nell – Business Card</title>
<link href="https://fonts.googleapis.com/css2?family=Roboto+Condensed:wght@300;400&family=Parisienne&display=swap" rel="stylesheet">
<style>
  :root {
    --backdrop: #b9b9bb;
    --card: #ffffff;
    --ink: #1a1a1a;
    --ink-soft: #3a3a3a;
    --sans: "Roboto Condensed", "Arial Narrow", sans-serif;
    --script: "Parisienne", cursive;
  }
  * { margin: 0; padding: 0; box-sizing: border-box; }
  html, body { width: 1200px; height: 900px; overflow: hidden; }
  body {
    background: var(--backdrop);
    position: relative;
    font-family: var(--sans);
    color: var(--ink);
  }
  .card {
    position: absolute;
    top: 300px;
    width: 520px;
    height: 297px;
    background: var(--card);
    overflow: hidden;
  }
  .card--front { left: 60px; }
  .card--back { left: 620px; }

  /* Front */
  .brand {
    position: absolute;
    top: 92px;
    left: 0;
    width: 100%;
    text-align: center;
  }
  .brand__mark {
    display: inline-block;
    width: 22px;
    height: 22px;
    border-radius: 50%;
    background: var(--ink);
    margin-bottom: 10px;
  }
  .brand__name {
    font-size: 30px;
    font-weight: 400;
    letter-spacing: 0.5px;
    line-height: 1;
  }
  .brand__service {
    font-size: 12px;
    font-weight: 300;
    margin-top: 4px;
    color: var(--ink-soft);
  }
  .tagline {
    position: absolute;
    top: 222px;
    left: 0;
    width: 100%;
    text-align: center;
    font-family: var(--script);
    font-size: 24px;
  }

  /* Back */
  .monogram-space {
    position: absolute;
    left: -70px;
    bottom: -90px;
    width: 250px;
    height: 250px;
    border-radius: 50%;
    background: var(--ink);
  }
  .contact {
    position: absolute;
    top: 34px;
    left: 270px;
  }
  .contact__name {
    font-size: 24px;
    font-weight: 400;
    margin-bottom: 6px;
  }
  .contact__line {
    font-size: 13px;
    font-weight: 300;
    line-height: 1.3;
  }
  .services {
    position: absolute;
    top: 140px;
    left: 340px;
    list-style: none;
    font-size: 11px;
    font-weight: 300;
    line-height: 1.45;
  }
  .services li::before {
    content: "\2022";
    margin-right: 5px;
  }
</style>
</head>
<body>
  <section class="card card--front">
    <div class="brand">
      <span class="brand__mark"></span>
      <h1 class="brand__name">HOPSCOTCH NELL</h1>
      <p class="brand__service">Personal Concierge &amp; Errand Service</p>
    </div>
    <p class="tagline">we hopscotch so you dont have to!</p>
  </section>

  <section class="card card--back">
    <div class="monogram-space"></div>
    <div class="contact">
      <h2 class="contact__name">Nellie Calloway</h2>
      <p class="contact__line">P : 583.402.9176</p>
      <p class="contact__line">E : nellie@hopscotchnell.biz</p>
      <p class="contact__line">www.hopscotchnell.biz</p>
    </div>
    <ul class="services">
      <li>Personal Shopping &amp; Errand</li>
      <li>House Hold Management</li>
      <li>Corporate Concierge</li>
      <li>Project Management</li>
      <li>Group Rates for Teachers &amp; Seniors</li>
    </ul>
  </section>
</body>
</html>
```